Verpackungen für Duschbrausen
Zielgruppe
Wir verkaufen verschiedene Produkte über E-Commerce Plattformen. Zielgruppe sind in diesem Fall alle die eine neue Duschbrause benötigen.
Aufgabenstellung
Liebe Grafikerinnen und Grafiker,
wir werden eine neue Produktlinie von Duschbrausen auf den Markt bringen und benötigen dafür eine frische, ansprechende Umverpackung. Eure Kreativität und Expertise sind gefragt, um eine Verpackung zu gestalten, die sowohl für verschiedene Duschbrausenmodelle geeignet ist als auch neutral und ansprechend wirkt.
Unser Ziel ist es, eine Verpackung zu kreieren, die sich von anderen abhebt, aber dennoch einen gewissen Neutralitätsgrad beibehält. Die Verpackung sollte modern, professionell und ansprechend gestaltet sein, um die Aufmerksamkeit der Kunden zu gewinnen.
Im Anhang findet ihr Beispiele von anderen Firmen (Zip Datei Verpackung Mitbewerber), wie sie ihre Duschbrausen verpacken. Diese dienen lediglich zur Inspiration und sollen euch einen Einblick in den aktuellen Markt geben. Wir ermutigen euch jedoch dazu, eure eigenen kreativen Ideen einzubringen und eine einzigartige Umverpackung zu entwerfen.
Bitte beachtet bei euren Entwürfen folgende Punkte:
Neutralität: Die Verpackung sollte für verschiedene Duschbrausenmodelle geeignet sein.
Modernität: Ein zeitgemäßes Design
Ansprechendes Layout: Klare Strukturen und gut lesbare Informationen.
Wir sind sehr gespannt auf eure Vorschläge :-)
Bei Fragen oder Unklarheiten stehe ich euch gerne zur Verfügung. Vielen Dank im Voraus für eure kreative Arbeit!
Mit freundlichen Grüßen,
Bertold

```html
<!DOCTYPE html>
<html lang="de">
<head>
<meta charset="utf-8">
<title>NEVRA – Faltschachtel Duschkopf</title>
<link rel="stylesheet" href="https://fonts.googleapis.com/css2?family=Raleway:wght@300;400&family=Archivo:wght@400;600&display=swap">
<style>
  :root{
    --page:#f4f4f4;
    --navy:#0a2452;
    --ink:#03060f;
    --rose:#c7aaa4;
    --text:#0b1e45;
    --white:#ffffff;
    --line:#3a3a3a;
    --chrome-a:#e9ecef;
    --chrome-b:#9aa0a8;
  }
  html,body{margin:0;padding:0;width:1200px;height:1200px;overflow:hidden;background:var(--page);}
  .dieline{display:block;width:1200px;height:1200px;}
  .cut{fill:none;stroke:var(--line);stroke-width:1;}
  .panel-white{fill:var(--white);stroke:var(--line);stroke-width:1;}
  .navy{fill:var(--navy);}
  .ink{fill:var(--ink);}
  .wordmark{font-family:"Raleway",sans-serif;font-weight:400;fill:var(--text);}
  .headline{font-family:"Raleway",sans-serif;font-weight:300;fill:var(--rose);}
  .tagline{font-family:"Archivo",sans-serif;font-weight:400;fill:var(--text);font-size:19px;letter-spacing:2px;}
  .size-note{font-family:"Archivo",sans-serif;font-size:14px;fill:var(--rose);letter-spacing:1px;}
  .copy-title{font-family:"Archivo",sans-serif;font-weight:600;font-size:14px;fill:var(--text);letter-spacing:1px;}
  .copy-body{font-family:"Archivo",sans-serif;font-weight:400;font-size:13.5px;fill:var(--text);letter-spacing:.6px;}
  .mode-label{font-family:"Archivo",sans-serif;font-size:17px;fill:var(--rose);letter-spacing:2px;}
  .mode-icon{fill:url(#chrome);stroke:#555;stroke-width:1;}
  .badge{fill:none;stroke:var(--rose);stroke-width:1.5;}
  .hang-hole{fill:none;stroke:#5a6a8a;stroke-width:1;}
  .product{fill:url(#chrome);}
</style>
</head>
<body>
<svg class="dieline" viewBox="30 40 1140 1160" preserveAspectRatio="xMidYMid meet" xmlns="http://www.w3.org/2000/svg">
  <defs>
    <linearGradient id="chrome" x1="0" y1="0" x2="1" y2="1">
      <stop offset="0" stop-color="var(--chrome-a)"/>
      <stop offset="1" stop-color="var(--chrome-b)"/>
    </linearGradient>
  </defs>

  <!-- glue flap -->
  <path class="panel-white" d="M105 270 L60 282 L60 1045 L105 1055 Z"/>

  <!-- back panel -->
  <g class="back-panel">
    <path class="navy" d="M109 62 L329 62 L329 1183 L195 1183 L195 1140 L105 1055 L105 66 Z"/>
    <path class="ink" d="M329 62 L458 62 L462 66 L462 1055 L372 1140 L372 1183 L329 1183 Z"/>
    <line class="hang-hole" x1="105" y1="105" x2="329" y2="105"/>
    <line class="hang-hole" x1="105" y1="188" x2="329" y2="188"/>
    <line class="hang-hole" x1="105" y1="270" x2="462" y2="270"/>
    <path class="hang-hole" d="M248 142 H270 Q275 132 285 132 Q295 132 300 142 H320 Q329 142 329 151 Q329 160 320 160 H248 Q240 160 240 151 Q240 142 248 142 Z"/>
    <path class="hang-hole" d="M248 215 H270 Q275 205 285 205 Q295 205 300 215 H320 Q329 215 329 224 Q329 233 320 233 H248 Q240 233 240 224 Q240 215 248 215 Z"/>
    <path fill="var(--white)" d="M105 370 Q190 345 270 362 Q360 385 462 368 L462 722 Q390 735 330 722 Q230 700 105 722 Z"/>
    <rect class="cut" x="105" y="270" width="357" height="785"/>

    <circle cx="180" cy="455" r="6" fill="#c33"/>
    <text class="copy-title" x="198" y="460">DAS VOLLE PROGRAMM.</text>
    <text class="copy-body" x="172" y="478">Unsere multifunktionale Brause</text>
    <text class="copy-body" x="172" y="496">bietet dir fünf verschiedene Ein-</text>
    <text class="copy-body" x="172" y="513">stellungen – ganz wie im Urlaub.</text>

    <circle cx="180" cy="591" r="6" fill="#2a3f8a"/>
    <text class="copy-title" x="198" y="596">THE WHOLE NINE YARDS.</text>
    <text class="copy-body" x="172" y="614">Our multifunctional shower head</text>
    <text class="copy-body" x="172" y="631">offers you five different settings</text>
    <text class="copy-body" x="172" y="648">– just like on holiday.</text>

    <g class="modes" text-anchor="end">
      <text class="mode-label" x="309" y="785">RAINFALL.</text>
      <text class="mode-label" x="309" y="842">WATERFALL MIST.</text>
      <text class="mode-label" x="309" y="898">MASSAGE.</text>
      <text class="mode-label" x="309" y="942">RAINFALL +</text>
      <text class="mode-label" x="309" y="964">MASSAGE</text>
      <text class="mode-label" x="309" y="1002">RAINFALL +</text>
      <text class="mode-label" x="309" y="1024">WATERFALL MIST.</text>
    </g>
    <circle class="mode-icon" cx="370" cy="778" r="21" role="img" aria-label="Symbolbild Strahlart Rainfall"/>
    <circle class="mode-icon" cx="370" cy="835" r="21" role="img" aria-label="Symbolbild Strahlart Waterfall Mist"/>
    <circle class="mode-icon" cx="370" cy="891" r="21" role="img" aria-label="Symbolbild Strahlart Massage"/>
    <circle class="mode-icon" cx="370" cy="947" r="21" role="img" aria-label="Symbolbild Strahlart Rainfall und Massage"/>
    <circle class="mode-icon" cx="370" cy="1007" r="21" role="img" aria-label="Symbolbild Strahlart Rainfall und Waterfall Mist"/>
  </g>

  <!-- left side panel -->
  <g class="side-left">
    <path class="panel-white" d="M478 160 L607 160 L615 245 L625 255 L625 270 L462 270 Z"/>
    <rect class="panel-white" x="462" y="270" width="163" height="785"/>
    <path class="panel-white" d="M462 1055 L625 1055 L543 1140 L543 1183 L462 1183 Z"/>
    <text class="wordmark" font-size="46" transform="translate(562 782) rotate(-90)" textLength="238" lengthAdjust="spacing">NEVRA</text>
  </g>

  <!-- right side panel -->
  <g class="side-right">
    <path class="panel-white" d="M998 160 L1128 160 L1145 270 L982 270 L982 255 L992 245 Z"/>
    <rect class="panel-white" x="982" y="270" width="163" height="785"/>
    <path class="cut" d="M982 1055 L1040 1112"/>
    <text class="tagline" transform="translate(1070 825) rotate(-90)">DEIN URLAUB FÜR ZUHAUSE.</text>
  </g>

  <!-- front panel -->
  <g class="front-panel">
    <path class="panel-white" d="M629 62 L978 62 L982 66 L982 270 L625 270 L625 66 Z"/>
    <line class="cut" x1="625" y1="105" x2="982" y2="105"/>
    <text class="wordmark" font-size="46" x="684" y="180" textLength="238" lengthAdjust="spacing">NEVRA</text>

    <path class="ink" d="M625 230 Q690 205 758 206 L758 1140 L715 1140 L715 1183 L625 1183 L625 1055 L568 1055 Q610 820 602 640 Q595 420 605 270 L625 270 Z"/>
    <path class="navy" d="M758 206 Q870 212 982 208 L982 270 L1018 270 Q1040 500 1026 720 Q1015 900 1030 1055 L982 1055 L982 1183 L892 1183 L892 1140 L758 1140 Z"/>

    <text class="size-note" x="766" y="292">⌀ 115 MM</text>
    <circle class="badge" cx="705" cy="365" r="52"/>
    <circle class="badge" cx="705" cy="365" r="36"/>

    <g class="product" role="img" aria-label="Produktfoto: verchromter Handbrausekopf mit fünf Strahlarten">
      <circle cx="772" cy="520" r="134"/>
      <rect x="662" y="610" width="84" height="440" rx="40"/>
    </g>

    <text class="headline" font-size="60" transform="translate(822 1020) rotate(-90)" textLength="140">5IN1</text>
    <text class="headline" font-size="60" transform="translate(875 1020) rotate(-90)" textLength="318">MASSAGE</text>
    <text class="headline" font-size="102" transform="translate(962 1018) rotate(-90)" textLength="698">DUSCHKOPF</text>

    <rect class="cut" x="625" y="270" width="357" height="785"/>
  </g>
</svg>
</body>
</html>
```